Diet, Exercise, & Friends are Associated with Parkinson's disease Progression

We are researchers looking for modifiable variables associated with different rates of Parkinson's disease (PD) progression. This is a novel scale: www.VELKAM.org -- higher scores are associated with worse quality of life. Low is good. High is bad. Each of the dots is a real person (maybe those should disappear?). The line represents the typical rate of PD progression over time. Color scheme of different degrees of quality of life can change, but the general concept seems to be working. (see updated version at the bottom of the www.VELKAM.org website)We need to combine the exercise data from here. This poster was essentially my attempt at an infographic for scientists:https://files.exampledrop.net/static/7a21c4e9b0d3f5a6c8e1d2b4/t/8c33d1a7e5f2b9c4d6a1e7f3/2047719385210/TRV2017+Diet.pdf. The updated data is in the uploaded figure below. Please use this list/ verbage!I don't necessarily need to stick to red=bad, green=good, but that's the best I've been able to come up with to communicate all this. I can get the actual data output later, but it might be nice to be able to demonstrate intensity. Veggies are quite a bit better than spices. Loneliness is much, much worse than pasta. This is the original published data. We have updated data and want to turn it into an infographic (while we work on a new manuscript).https://www.quorvel.net/journals/jrbt/2017/8173920/
Target Market(s)
Individuals age 40-80 with Parkinson's disease (and their friends & family members).
Neurologists should be handing this out in their offices.
When patients ask their physician about nutrition, etc., we want this to be the 1-pg handout they give them.
Industry/Entity Type
Medicine
Font styles to use
Colors
Designer to choose colors to be used in the design.
Requirements
Must have
- VEL-KAM scale (www.VELKAM.org)-- use this picture on top. OK to change color.
- Lists foods/ activities associated with different rates of progression
- Title: "Food, Friends, and Exercise: Lifestyle Associations with PD Progression"
- Legend/ disclaimer (smaller font):
- "All results were adjusted for age, gender, and years since diagnosis. Total sample size: 1600+
- Based on the methods described in publication: "Effects of Meal Timing and Herbal Additives on Tremor Course" [Dunwarth RT et al, Jrnl Biol Tiss Rsch 2017], an updated analysis was performed on data on 7 May 2019. (N >1600)"
- "VEL-KAM scores available at www.VELKAM.org"
- Must fit on a single 8.5 x 11" page.
Nice to have
- The background should be white-- I want neurologists/ physicians downloading it, printing it, and distributing to patients. I don't want to waste ink.
- Logo for Wexmoor College and/or the logo for the "LUN Grove TR" Study. I like the WC emblem in one corner and the picture at the top of this website: www.VELKAM.org
- Would be nice if it could be understood between cultures and/ or easily translated.
- Would be nice if we could invite people to participate in the study!
- "To learn about joining the study, please to www.LUNGroveTR.wexmoor.edu"
Should not have
- Pictures of overweight people, or the impression that a muscular white guy is the ideal. I want to leave room for diversity and flexible interpretation.
- Too much text- a good-sized portion of this group will have poor vision and/or dementia. Needs to be simple.
- I like the simplicity of "Good" and "Bad"... don't love the labels. Seems to 'jugdgy'. Maybe "Encourage" and "Avoid" OR "Positive" and "Negative"

```html
<!DOCTYPE html>
<html lang="en">
<head>
<meta charset="utf-8">
<title>Foods, Friends &amp; Exercise: Lifestyle Associations with Parkinson Progression</title>
<link href="https://fonts.googleapis.com/css2?family=Montserrat:wght@600;700&family=Arimo:wght@400;700&display=swap" rel="stylesheet">
<style>
  :root{
    --frame:#a33a2e;
    --ink:#1e1e1e;
    --avoid:#a85a4c;
    --encourage:#8cc24a;
    --band-poor:#e9d3d5;
    --band-fair:#e8b291;
    --band-good:#b0bfdc;
    --band-excellent:#d1e2b8;
    --college:#7b2a1f;
    --study-ring:#5457a3;
    --study-fill:#a9cdee;
  }
  html,body{margin:0;padding:0;overflow:hidden;background:#fff;}
  .poster{position:relative;width:1200px;height:936px;overflow:hidden;background:#fff;color:var(--ink);font-family:"Arimo",Arial,sans-serif;}
  .frame{position:absolute;left:12px;top:16px;width:1174px;height:904px;border:1.6px solid var(--frame);border-radius:18px;box-sizing:border-box;}
  .title{position:absolute;left:0;right:0;top:30px;margin:0;text-align:center;font-family:"Montserrat",Arial,sans-serif;font-weight:700;font-size:35px;line-height:37px;letter-spacing:.3px;}
  .intro{position:absolute;left:130px;top:146px;width:650px;font-size:17.2px;line-height:20px;margin:0;}
  .intro h2{font-size:17.2px;margin:0;font-weight:700;}
  .intro p{margin:0 0 20px;}
  .partners{position:absolute;top:178px;left:856px;width:280px;display:flex;justify-content:space-between;}
  .partner{width:130px;display:flex;flex-direction:column;align-items:center;}
  .partner-dot{width:84px;height:84px;border-radius:50%;}
  .partner-dot.college{background:var(--college);}
  .partner-dot.study{background:var(--study-fill);}
  .partner-name{margin-top:8px;font-size:14px;font-weight:700;color:var(--ink);text-align:center;}
  .chart{position:absolute;left:0;top:380px;}
  .lists{position:absolute;left:0;top:0;}
  .group-icon{position:absolute;width:34px;height:34px;}
  .item{position:absolute;font-size:15.2px;line-height:18px;white-space:nowrap;}
  .item::before{content:"";position:absolute;left:-13px;top:5px;width:8px;height:8px;border-radius:50%;}
  .avoid::before{background:var(--avoid);}
  .encourage::before{background:var(--encourage);}
  .footnote{position:absolute;left:0;right:0;top:894px;text-align:center;font-size:15.2px;margin:0;}
</style>
</head>
<body>
<div class="poster">
  <div class="frame"></div>
  <h1 class="title">Foods, Friends &amp; Exercise:&nbsp; Lifestyle Associations<br>with Parkinson Progression</h1>

  <div class="intro">
    <h2>Measuring PD Progression</h2>
    <p>Individuals with Parkinson's are asked to describe the severity of 34 common symptoms. 0= healthy - 100= severe. High scores are associated with a lower reported quality of life. The lower your VEL-KAM score, the better!</p>
    <p>LUN Grove TR is an ongoing "big data" study designed to describe modifiable variables associated with RATE of progression.&nbsp; Results presented here are based on data collected between 27 March 2012 - 27 May 2019. All analyses have been adjusted for age, gender, and years since diagnosis according to the methods described in Effects of Meal Timing and Herbal Additives on Tremor Course."</p>
  </div>

  <div class="partners">
    <div class="partner"><div class="partner-dot college"></div><div class="partner-name">Wexmoor College</div></div>
    <div class="partner"><div class="partner-dot study"></div><div class="partner-name">LUN Grove TR</div></div>
  </div>

  <svg class="chart" width="800" height="500" viewBox="0 380 800 500" font-family="Arimo, Arial, sans-serif">
    <text x="438" y="409" text-anchor="middle" font-family="Montserrat, Arial, sans-serif" font-weight="700" font-size="22">Patient-Reported Outcomes in PD (VEL-KAM)</text>
    <rect x="140" y="430" width="626" height="147" fill="var(--band-poor)"/>
    <rect x="140" y="577" width="626" height="73" fill="var(--band-fair)"/>
    <rect x="140" y="650" width="626" height="73" fill="var(--band-good)"/>
    <rect x="140" y="723" width="626" height="73" fill="var(--band-excellent)"/>
    <g stroke="#fff" stroke-width="1.4">
      <line x1="140" y1="577" x2="766" y2="577"/><line x1="140" y1="650" x2="766" y2="650"/>
      <line x1="140" y1="723" x2="766" y2="723"/><line x1="140" y1="506" x2="766" y2="506"/>
      <line x1="255.5" y1="430" x2="255.5" y2="796"/><line x1="371" y1="430" x2="371" y2="796"/>
      <line x1="486.5" y1="430" x2="486.5" y2="796"/><line x1="602" y1="430" x2="602" y2="796"/>
      <line x1="717.5" y1="430" x2="717.5" y2="796"/>
    </g>
    <polygon points="150,701 766,525 766,577 150,704" fill="#fff" fill-opacity=".75"/>
    <line x1="148" y1="702" x2="756" y2="555" stroke="var(--avoid)" stroke-width="3.5" stroke-dasharray="11 6"/>
    <rect x="510" y="442" width="186" height="40" fill="#fff"/>
    <text x="603" y="471" text-anchor="middle" font-family="Montserrat, Arial, sans-serif" font-weight="600" font-size="22">Quality of Life</text>
    <g font-family="Montserrat, Arial, sans-serif" font-weight="600" font-size="19" text-anchor="middle">
      <text x="606" y="528">Poor</text><text x="602" y="634">Fair</text>
      <text x="602" y="695">Good</text><text x="603" y="765">Excellent</text>
    </g>
    <g font-weight="700" font-size="19" text-anchor="end">
      <text x="128" y="437">2,500</text><text x="128" y="513">2,000</text><text x="128" y="584">1,500</text>
      <text x="128" y="657">1,000</text><text x="128" y="731">500</text><text x="122" y="800">0</text>
    </g>
    <text transform="translate(54 608) rotate(-90)" text-anchor="middle" font-family="Montserrat, Arial, sans-serif" font-weight="700" font-size="22">VEL-KAM Score</text>
    <g font-weight="700" font-size="19" text-anchor="middle">
      <text x="142" y="822">0</text><text x="254" y="822">5</text><text x="371" y="822">10</text>
      <text x="486" y="822">15</text><text x="602" y="822">20</text><text x="715" y="822">25</text>
    </g>
    <text x="450" y="858" text-anchor="middle" font-family="Montserrat, Arial, sans-serif" font-weight="700" font-size="22">Years Since Diagnosis</text>
  </svg>

  <svg class="lists" width="1200" height="936" viewBox="0 0 1200 936" aria-hidden="true">
    <defs>
      <g id="icon-person"><circle cx="0" cy="-5" r="5" fill="none" stroke="#fff" stroke-width="2.2"/><path d="M-9 9 v-2 a6 6 0 0 1 6 -5 h6 a6 6 0 0 1 6 5 v2 z" fill="none" stroke="#fff" stroke-width="2.2"/></g>
      <g id="icon-food" stroke="#fff" stroke-width="2.4" stroke-linecap="round" fill="none"><line x1="-8" y1="9" x2="7" y2="-7"/><path d="M4 -10 l6 6"/><line x1="8" y1="9" x2="-6" y2="-5"/><ellipse cx="-7" cy="-7" rx="3" ry="5" transform="rotate(-45 -7 -7)"/></g>
      <g id="icon-heart"><path d="M0 10 C-14 1 -12 -10 -5 -10 C-2 -10 0 -7 0 -6 C0 -7 2 -10 5 -10 C12 -10 14 1 0 10z" fill="#fff"/><polyline points="-11,0 -5,0 -3,-5 0,5 2,-2 4,0 11,0" fill="none" stroke="currentColor" stroke-width="1.8"/></g>
    </defs>
    <g color="var(--avoid)">
      <circle cx="814" cy="436" r="17" fill="var(--avoid)"/><use href="#icon-person" x="814" y="436"/>
      <circle cx="814" cy="502" r="17" fill="var(--avoid)"/><use href="#icon-food" x="814" y="502"/>
      <circle cx="814" cy="565" r="17" fill="var(--avoid)"/><use href="#icon-heart" x="814" y="566"/>
    </g>
    <g color="var(--encourage)">
      <circle cx="814" cy="646" r="17" fill="var(--encourage)"/><use href="#icon-person" x="814" y="646"/>
      <circle cx="814" cy="718" r="17" fill="var(--encourage)"/><use href="#icon-food" x="814" y="718"/>
      <circle cx="814" cy="796" r="17" fill="var(--encourage)"/><use href="#icon-heart" x="814" y="797"/>
    </g>
  </svg>

  <div class="item avoid" style="left:862px;top:412px">“I’m overweight.”</div>
  <div class="item avoid" style="left:862px;top:430px">“I’m lonely.”</div>
  <div class="item avoid" style="left:864px;top:461px">Dairy</div>
  <div class="item avoid" style="left:864px;top:480px">Beef</div>
  <div class="item avoid" style="left:864px;top:498px">Chicken</div>
  <div class="item avoid" style="left:864px;top:517px">Soda</div>
  <div class="item avoid" style="left:966px;top:461px">Fried foods</div>
  <div class="item avoid" style="left:966px;top:480px">Canned fruits</div>
  <div class="item avoid" style="left:966px;top:498px">Canned vegetables</div>
  <div class="item avoid" style="left:966px;top:517px">Frozen vegetables</div>
  <div class="item avoid" style="left:864px;top:550px">No benefit associated to<br>0-2 days/week of exercise</div>

  <div class="item encourage" style="left:858px;top:617px">“I have lots of friends.”</div>
  <div class="item encourage" style="left:858px;top:636px">“I try to eat organic when possible.”</div>
  <div class="item encourage" style="left:858px;top:654px">“I cook most of my own meals.”</div>
  <div class="item encourage" style="left:861px;top:684px">Fresh vegetables</div>
  <div class="item encourage" style="left:861px;top:703px">Olive &amp; coconut oil</div>
  <div class="item encourage" style="left:861px;top:721px">Nuts &amp; seeds</div>
  <div class="item encourage" style="left:861px;top:740px">Non-fried fish</div>
  <div class="item encourage" style="left:1041px;top:682px">Fresh fruit</div>
  <div class="item encourage" style="left:1041px;top:701px">Fresh herbs</div>
  <div class="item encourage" style="left:1041px;top:719px">Spices</div>
  <div class="item encourage" style="left:1041px;top:738px">Wine</div>
  <div class="item encourage" style="left:858px;top:769px">7 days/week of exercise is better than 6</div>
  <div class="item encourage" style="left:858px;top:788px">6 days/week of exercise is better than 5…</div>
  <div class="item encourage" style="left:858px;top:806px">Trend continues to 3 days/week</div>

  <p class="footnote">All results adjusted for age, gender, and years since diagnosis. Total sample size: 1600+. Updated dataset as of 7 May 2019.</p>
</div>
</body>
</html>
```